Simple Business Cards for Self-employed Coach

Simple business card with a design that includes the QLT logo.
Using either only the logo color or additional colors that match the logo.

Meridian Guides reach deeply into the past, gathering wisdom from East and West, while still staying current with the frontiers of new discovery in cognitive science, genetics, and other disciplines. see https://www.brightharborpath.example/what-is-integral-coaching/

Target Market(s)

Coaching Clients in Tokyo /Asia; in business organizations, but also outside

Industry/Entity Type

Life Coaching

Contact Information for Business Card

Lukas Brenning
Certified Meridian Guide

3-2-48 Kamiyoshi
Nakarino 164-0392
Tokyo, Japan

Phone: +81 70 4817 5062
E-Mail: lukas.brenning@mailora.example

Font styles to use
Sans Serif

Colors
00a990

Requirements
Must have
• include uploaded logo
• color fitting with QLT logo color
Nice to have
• simple, elegant design
Should not have
• clutter

```html
<!DOCTYPE html>
<html lang="en">
<head>
<meta charset="utf-8">
<title>Lukas Brenning – Business Card</title>
<link rel="stylesheet" href="https://fonts.googleapis.com/css2?family=PT+Sans:wght@400;700&display=swap">
<style>
  :root {
    --teal: #04776f;
    --teal-shade: #03615a;
    --paper: #ffffff;
    --backdrop: #e4dfdf;
    --ghost: rgba(20, 40, 40, 0.07);
  }
  * { margin: 0; padding: 0; box-sizing: border-box; }
  html, body { width: 1200px; height: 800px; overflow: hidden; }
  body {
    background: var(--backdrop);
    font-family: "PT Sans", sans-serif;
    position: relative;
  }
  .card {
    position: absolute;
    left: 75px; top: 100px;
    width: 1050px; height: 600px;
    background: var(--paper);
    overflow: hidden;
    box-shadow: 0 10px 30px rgba(0,0,0,0.12);
  }
  .card-shapes { position: absolute; inset: 0; }
  .brand-box {
    position: absolute;
    left: 36px; top: 34px;
    width: 300px; height: 120px;
    background: var(--paper);
    display: flex; align-items: center; justify-content: center; gap: 18px;
  }
  .brand-mark { width: 26px; height: 26px; background: var(--teal); }
  .brand-name {
    color: var(--teal);
    font-weight: 700;
    font-size: 62px;
    letter-spacing: 10px;
  }
  .brand-ghost {
    position: absolute;
    left: 470px; top: 110px;
    font-size: 250px;
    font-weight: 700;
    letter-spacing: 40px;
    color: var(--ghost);
    line-height: 1;
  }
  .identity { position: absolute; left: 630px; top: 250px; text-align: center; }
  .person-name { color: var(--teal); font-weight: 700; font-size: 44px; }
  .person-title { color: var(--teal); font-size: 21px; margin-top: 2px; }
  .contacts {
    position: absolute; left: 585px; top: 390px;
    list-style: none; color: var(--teal); font-size: 25px; line-height: 1.25;
  }
  .contacts li { display: flex; gap: 22px; margin-bottom: 18px; }
  .contacts svg { width: 30px; height: 30px; flex: none; margin-top: 2px; }
</style>
</head>
<body>
  <article class="card">
    <svg class="card-shapes" viewBox="0 0 1050 600" aria-hidden="true">
      <rect width="1050" height="600" fill="var(--teal)"/>
      <ellipse cx="1000" cy="300" rx="640" ry="520" fill="var(--teal-shade)" transform="translate(-40 30)"/>
      <ellipse cx="1000" cy="270" rx="660" ry="560" fill="var(--paper)" transform="translate(0 0)"/>
    </svg>
    <div class="brand-ghost" aria-hidden="true">QLT</div>
    <div class="brand-box">
      <span class="brand-mark"></span>
      <span class="brand-name">QLT</span>
    </div>
    <div class="identity">
      <h1 class="person-name">Lukas Brenning</h1>
      <p class="person-title">Certified Meridian Guide</p>
    </div>
    <ul class="contacts">
      <li>
        <svg viewBox="0 0 24 24"><circle cx="12" cy="12" r="12" fill="var(--teal)"/><path d="M8 6.5l2 2-1.2 1.6a8 8 0 0 0 5.1 5.1l1.6-1.2 2 2-1.3 1.6c-4.6-.4-8.7-4.5-9.1-9.1z" fill="#fff"/></svg>
        <span>+81 70 4817 5062</span>
      </li>
      <li>
        <svg viewBox="0 0 24 24"><circle cx="12" cy="12" r="12" fill="var(--teal)"/><rect x="6" y="8" width="12" height="8" rx="1" fill="#fff"/><path d="M6 9l6 4 6-4" stroke="var(--teal)" stroke-width="1.2" fill="none"/></svg>
        <span>lukas.brenning@mailora.example</span>
      </li>
      <li>
        <svg viewBox="0 0 24 24"><path d="M12 1a8 8 0 0 0-8 8c0 6 8 14 8 14s8-8 8-14a8 8 0 0 0-8-8z" fill="var(--teal)"/><circle cx="12" cy="9" r="3" fill="#fff"/></svg>
        <span>3-2-48 Kamiyoshi<br>Nakarino 164-0392<br>Tokyo, Japan</span>
      </li>
    </ul>
  </article>
</body>
</html>
```